Psychiatrist/ Psychotherapist needs a letterhead design

I am a Psychiatrist working in private practice. I work as a psychotherapist and treat patients with depression, anxiety, post traumatic stress and relationship problems. I need a letterhead which is elegant and professional. I would like to see designs using colours such as blues and greys.
I would like the information on the letterhead split between the top and bottom of the page to give it a look of balance.
I want it to look elegant, feminine and upmarket. I don't want it to look too corporate but to show some flair and to be a bit artistic.

Target Market(s)

Other doctors, specialists and agencies who have referred patients to me.

Industry/Entity Type

Work

Font styles to use
Script

Requirements
Must have
• My name and my profession psychiatrist need to be highlighted and prominent. It needs to be professional looking and elegant without being old fashioned or too conservative.
Nice to have
• Balance between the top and bottom of the page.
Should not have
• I don't want fonts which are old and too traditional.

```html
<!DOCTYPE html>
<html lang="en">
<head>
<meta charset="utf-8">
<title>Dr Miriam Ashcombe B. – Letterhead</title>
<link rel="stylesheet" href="https://fonts.googleapis.com/css2?family=Cinzel:wght@500&family=Questrial&display=swap">
<style>
  :root {
    --backdrop: #d9d9d9;
    --paper: #ffffff;
    --accent-blue: #1a8fb8;
    --name-blue: #1b86b3;
    --text-grey: #6f6f6f;
    --divider-grey: #9a9a9a;
    --band-green: #12924a;
  }
  html, body {
    margin: 0;
    padding: 0;
    width: 1200px;
    height: 968px;
    overflow: hidden;
    background: var(--backdrop);
  }
  .letterhead {
    position: absolute;
    left: 282px;
    top: 34px;
    width: 636px;
    height: 900px;
    background: var(--paper);
    box-shadow: 0 2px 10px rgba(0,0,0,0.12);
  }
  .letterhead__marker {
    position: absolute;
    left: 0;
    top: 34px;
    width: 9px;
    height: 34px;
    background: var(--accent-blue);
  }
  .letterhead__identity {
    position: absolute;
    left: 44px;
    top: 34px;
  }
  .identity__name {
    margin: 0;
    font-family: "Cinzel", serif;
    font-weight: 500;
    font-size: 21px;
    letter-spacing: 0.5px;
    color: var(--name-blue);
    line-height: 1.05;
  }
  .identity__profession {
    margin: 2px 0 0;
    font-family: "Questrial", sans-serif;
    font-size: 15px;
    color: var(--text-grey);
  }
  .letterhead__contact {
    position: absolute;
    left: 40px;
    right: 40px;
    bottom: 30px;
    display: flex;
    justify-content: space-between;
    align-items: center;
    font-family: "Questrial", sans-serif;
    font-size: 9.5px;
    color: var(--text-grey);
    white-space: nowrap;
  }
  .contact__label {
    color: var(--accent-blue);
    font-weight: 700;
  }
  .contact__divider {
    color: var(--divider-grey);
  }
  .letterhead__band {
    position: absolute;
    left: 0;
    right: 0;
    bottom: 0;
    height: 12px;
    background: var(--band-green);
  }
</style>
</head>
<body>
  <main class="letterhead">
    <div class="letterhead__marker"></div>
    <header class="letterhead__identity">
      <h1 class="identity__name">Dr Miriam Ashcombe B.</h1>
      <p class="identity__profession">Psychiatrist</p>
    </header>

    <footer class="letterhead__contact">
      <span class="contact__item">12 Elm Street, Norwood, SA 5067</span>
      <span class="contact__divider">|</span>
      <span class="contact__item"><span class="contact__label">T:</span> (08) 8000 1234</span>
      <span class="contact__divider">|</span>
      <span class="contact__item"><span class="contact__label">F:</span> (08) 8000 5678</span>
      <span class="contact__divider">|</span>
      <span class="contact__item"><span class="contact__label">M:</span> 0400111222</span>
      <span class="contact__divider">|</span>
      <span class="contact__item"><span class="contact__label">E:</span> mashcombe@example.net</span>
    </footer>
    <div class="letterhead__band"></div>
  </main>
</body>
</html>
```